Image Ads needed for a Pharmacy Education e-commerce website

I need image ads with these specifications:

Supported formats: JPG, PNG, GIF
File size: 3MB max
Recommended aspect ratios: 1:1 square; 4:5 portrait; 4:3 landscape; 16:9 landscape
Recommended resolutions: 1080x1080 square, 1080x1350 portrait, 1440x1080 landscape, 1920x1080 landscape
Thumbnail: Displays at 400x300 pixels
Thumbnail file size: 500KB max

```html
<!DOCTYPE html>
<html lang="en">
<head>
<meta charset="utf-8">
<title>Dosewise – Unlimited PCEB CEUs $39</title>
<link rel="stylesheet" href="https://fonts.googleapis.com/css2?family=Varela+Round&family=Exo+2:wght@800&display=swap">
<style>
  :root {
    --navy: #233b5e;
    --navy-dark: #0e3345;
    --blue: #1470a8;
    --blue-deep: #0b3c66;
    --green: #6fa021;
    --green-soft: #72a545;
    --orange: #e0903c;
    --orange-light: #eab077;
    --white: #ffffff;
  }
  html, body {
    margin: 0;
    padding: 0;
    width: 1200px;
    height: 1200px;
    overflow: hidden;
    background: var(--white);
  }
  .ad {
    position: relative;
    width: 1200px;
    height: 1200px;
    overflow: hidden;
    background: var(--white);
    font-family: "Varela Round", sans-serif;
  }
  .brand {
    position: absolute;
    left: 82px;
    top: 98px;
    display: flex;
    align-items: center;
    gap: 18px;
    font-size: 104px;
    line-height: 1;
    color: var(--navy);
    letter-spacing: -2px;
  }
  .brand-dot {
    width: 34px;
    height: 34px;
    border-radius: 50%;
    background: var(--green-soft);
  }
  .offer {
    position: absolute;
    left: 0;
    top: 288px;
    width: 714px;
    height: 514px;
    background: var(--orange);
    overflow: hidden;
    color: var(--white);
  }
  .offer-glow {
    position: absolute;
    left: 578px;
    top: -20px;
    width: 400px;
    height: 440px;
    border-radius: 50%;
    background: var(--orange-light);
  }
  .offer-text {
    position: absolute;
    left: 80px;
    margin: 0;
    line-height: 1;
    font-weight: 400;
  }
  .offer-title { top: 42px; font-size: 94px; -webkit-text-stroke: 2px var(--white); }
  .offer-sub { top: 158px; font-size: 78px; left: 76px; }
  .offer-price { top: 248px; font-size: 258px; left: 78px; letter-spacing: -4px; -webkit-text-stroke: 3px var(--white); }
  .scene {
    position: absolute;
    left: 700px;
    top: 168px;
    width: 430px;
    height: 646px;
    border-radius: 40px;
    background: linear-gradient(180deg, #f3f6fa 0%, #e4edf5 55%, #c9d5e3 100%);
  }
  .stripe {
    position: absolute;
    left: 0;
    top: 880px;
    width: 1200px;
    height: 14px;
    display: flex;
  }
  .stripe span { flex: 1; }
  .stripe .s1 { background: var(--blue-deep); }
  .stripe .s2 { background: var(--blue); }
  .stripe .s3 { background: var(--green); }
  .stripe .s4 { background: var(--orange); }
  .badges {
    position: absolute;
    left: 0;
    top: 930px;
    width: 1200px;
    height: 220px;
  }
  .badge-text {
    font-family: "Exo 2", sans-serif;
    font-weight: 800;
    fill: var(--white);
    text-anchor: middle;
  }
</style>
</head>
<body>
  <main class="ad">
    <div class="brand"><span class="brand-name">Dosewise</span><span class="brand-dot"></span></div>

    <section class="offer">
      <div class="offer-glow"></div>
      <h1 class="offer-text offer-title">Unlimited</h1>
      <p class="offer-text offer-sub">PCEB Ceus</p>
      <p class="offer-text offer-price">$39</p>
    </section>

    <div class="scene" role="img" aria-label="Illustration of two pharmacists in white lab coats, one holding a clipboard"></div>

    <div class="stripe"><span class="s1"></span><span class="s2"></span><span class="s3"></span><span class="s4"></span></div>

    <svg class="badges" viewBox="0 0 1200 220" width="1200" height="220" aria-label="Highlights">
      <defs>
        <clipPath id="clip-left"><ellipse cx="218" cy="110" rx="130" ry="100"/></clipPath>
        <clipPath id="clip-mid"><ellipse cx="600" cy="110" rx="130" ry="100"/></clipPath>
        <clipPath id="clip-right"><ellipse cx="982" cy="110" rx="130" ry="100"/></clipPath>
      </defs>

      <g class="badge badge-years">
        <ellipse cx="218" cy="110" rx="134" ry="104" fill="var(--navy-dark)"/>
        <g clip-path="url(#clip-left)">
          <rect x="80" y="0" width="280" height="110" fill="var(--blue)"/>
          <rect x="80" y="110" width="280" height="110" fill="var(--navy)"/>
        </g>
        <ellipse cx="218" cy="110" rx="118" ry="92" fill="none" stroke="var(--white)" stroke-width="1.5"/>
        <text class="badge-text" x="218" y="92" font-size="62">17</text>
        <text class="badge-text" x="218" y="158" font-size="42">Years</text>
      </g>

      <g class="badge badge-accredited" role="img" aria-label="Accreditation badge">
        <ellipse cx="600" cy="110" rx="134" ry="104" fill="var(--navy-dark)"/>
        <g clip-path="url(#clip-mid)">
          <rect x="460" y="0" width="280" height="110" fill="var(--green-soft)"/>
          <rect x="460" y="110" width="280" height="110" fill="var(--navy)"/>
        </g>
        <ellipse cx="600" cy="110" rx="118" ry="92" fill="none" stroke="var(--white)" stroke-width="1.5"/>
      </g>

      <g class="badge badge-reports">
        <ellipse cx="982" cy="110" rx="134" ry="104" fill="var(--navy-dark)"/>
        <g clip-path="url(#clip-right)">
          <rect x="840" y="0" width="280" height="110" fill="var(--orange)"/>
          <rect x="840" y="110" width="280" height="110" fill="var(--navy)"/>
        </g>
        <ellipse cx="982" cy="110" rx="118" ry="92" fill="none" stroke="var(--white)" stroke-width="1.5"/>
        <text class="badge-text" x="982" y="84" font-size="38">Reports</text>
        <text class="badge-text" x="982" y="158" font-size="42">CE/CME</text>
      </g>
    </svg>
  </main>
</body>
</html>
```